Trifold Brochure Design Project

We need a trifold brochure design for a company/product called VitaLens. We provide full-body MRI screening, along with blood chemistry and DNA analysis, followed by a consultation with the MD in a comfortable outpatient setting.
The facility is located in Seabright, Coastal State.
The concept is that people usually don't know about many diseases until they are far advanced and more difficult to treat. We offer early detection which leads to early treatment and better outcomes.
The concept should blend an emotional construct (do it for yourself or someone you love, the best gift is health, live longer to love longer, etc) with science to legitimize the service. (MRI, Blood Chemistry, DNA analysis and an MD to interpret)

Target Market(s)

Baby boomers and active middle-age men and women

Industry/Entity Type

It Company

Requirements
Must have
• Attractive middle age people enjoying life because they know they are healthy.
Services are provided 7-days a week in a comfortable outpatient setting. Everything is totally confidential.
VitaLens is a division of Coral Ridge Diagnostic Centers
Nice to have
• Some clinical imagery such as the doctor, the MRI machine or inferences that this is a clinical-based solution.
Extremely experienced, qualified and licensed Doctors and Technologists are involved.

```html
<!DOCTYPE html>
<html lang="en">
<head>
<meta charset="utf-8">
<title>VitaLens Trifold Brochure – Outside</title>
<link href="https://fonts.googleapis.com/css2?family=Questrial&display=swap" rel="stylesheet">
<style>
  :root {
    --navy: #004a80;
    --heading-blue: #1f4e82;
    --teal: #6fb0bd;
    --cream: #f8efe2;
    --ink: #222222;
    --white: #ffffff;
    --photo-warm: #e8d2bf;
    --photo-light: #f5efe9;
    --machine-grey: #9aa2a8;
  }
  * { margin: 0; padding: 0; box-sizing: border-box; }
  html, body { width: 1200px; height: 927px; overflow: hidden; background: var(--white); }
  body { font-family: "Questrial", "Century Gothic", sans-serif; color: var(--ink); }
  .brochure { position: relative; width: 1200px; height: 927px; }

  /* Left panel */
  .panel-info { position: absolute; left: 0; top: 0; width: 400px; height: 927px; background: var(--cream); overflow: hidden; }
  .info-wave { position: absolute; left: 0; top: 0; width: 400px; height: 927px; }
  .package-title { position: absolute; left: 16px; top: 21px; font-size: 21px; font-weight: 700; color: var(--heading-blue); letter-spacing: 0.3px; }
  .package-copy { position: absolute; left: 16px; top: 49px; width: 368px; font-size: 16.1px; line-height: 24.1px; color: var(--ink); }
  .contact-block { position: absolute; right: 18px; top: 809px; text-align: right; color: var(--white); font-size: 22.5px; line-height: 24.4px; font-style: normal; }

  /* Middle panel (mailer) */
  .panel-mailer { position: absolute; left: 400px; top: 0; width: 405px; height: 927px; }
  .stamp-box { position: absolute; left: 22px; top: 32px; width: 78px; height: 73px; border: 1.3px solid #333; }
  .recipient-address { position: absolute; left: 204px; top: 528px; transform-origin: 0 0; transform: rotate(-90deg); font-size: 16px; line-height: 24px; white-space: nowrap; color: var(--ink); }
  .return-address { position: absolute; left: 50px; top: 907px; transform-origin: 0 0; transform: rotate(-90deg); white-space: nowrap; color: var(--ink); }
  .return-brand { display: flex; align-items: center; gap: 8px; font-size: 40px; line-height: 40px; color: var(--navy); }
  .return-brand .brand-dot { width: 14px; height: 14px; border-radius: 50%; background: var(--teal); }
  .return-lines { font-size: 18px; line-height: 23px; }
  .mri-image { position: absolute; left: 220px; top: 650px; width: 165px; height: 275px; background: radial-gradient(ellipse at 40% 40%, #e9ecee 0%, #b9c0c5 40%, var(--machine-grey) 60%, rgba(255,255,255,0) 75%); }

  /* Right panel (cover) */
  .panel-cover { position: absolute; left: 805px; top: 0; width: 395px; height: 927px; }
  .cover-brand { position: absolute; left: 90px; top: 356px; display: flex; align-items: center; gap: 10px; font-size: 52px; line-height: 60px; color: var(--navy); }
  .cover-brand .brand-dot { width: 22px; height: 22px; border-radius: 50%; background: var(--teal); }
  .couple-photo { position: absolute; left: 0; top: 665px; width: 395px; height: 262px; background: linear-gradient(180deg, var(--photo-light) 0%, var(--photo-warm) 55%, #f2ece6 100%); }
</style>
</head>
<body>
<main class="brochure">

  <section class="panel-info">
    <svg class="info-wave" viewBox="0 0 400 927" aria-hidden="true">
      <path d="M0 776 C 150 770, 310 720, 400 634 L400 927 L0 927 Z" fill="var(--navy)"/>
    </svg>
    <h2 class="package-title">The Complete Package</h2>
    <p class="package-copy">In addition to scanning your body using high-resolution MRI, we also perform blood and DNA analysis to determine if you have the potential for disease, or very early proto-disease that is not yet observable. By analyzing the hundreds of MRI images, the blood chemistry and DNA analysis, our clinicians can provide you with a comprehensive “road map” of health for your entire body now, and into the future. We also offer individual exams on specific organ systems, extremities, gender-specific exams and specific pathology search. Once the analysis is complete, each VitaLensTM patient has the opportunity to sit with Dr. Hollis one-on-one for a 30-minute consultation. This consultation is invaluable and includes not only a complete review of your anatomy, physiology and any pathology found, but recommendations for a wide array of corrective actions from minor to major. Once complete, you are provided with a written report and DVD containing all the information and images acquired about your own body. Taking control of your health is now in your hands. Knowledge is the key, and Dr. Hollis can give you the knowledge you need.</p>
    <address class="contact-block">
      Phone Number<br>Address<br>Address, State, Zip<br>www.vitalens.com
    </address>
  </section>

  <section class="panel-mailer">
    <div class="stamp-box"></div>
    <div class="recipient-address">Name<br>Address<br>Address, State, Zip</div>
    <div class="return-address">
      <div class="return-brand">VitaLens<span class="brand-dot"></span></div>
      <div class="return-lines">Address<br>Seabright, Coastal State</div>
    </div>
    <div class="mri-image" role="img" aria-label="MRI scanner machine"></div>
  </section>

  <section class="panel-cover">
    <div class="cover-brand">VitaLens<span class="brand-dot"></span></div>
    <div class="couple-photo" role="img" aria-label="Smiling middle-aged couple in white robes relaxing together"></div>
  </section>

</main>
</body>
</html>
```